Toy Company Needs a Web Site For a New Toy

We need a web site for a new toy called "Zippa Loop Trike". The bike is a plastic, non motorized ride on toy for kids ages 1.5 - 5 years of age. The bike is being launched in three colors, red, blue and pink, though we may include a black option too.

For the web site we want something bold and colorful that communicates fun, therefore NO dull colors like black or grey. Nothing too cluttered. We want the site to attract the attention of kids but also give the parents a sense of confidence in our professionalism as a trustworthy toy company. The home page should focus on the bike, with different views of the bike and a small write-up on some of its key features. We would also like the home page to have a video of the bike in play. A obvious link to the shopping basket must be present as well. The site must include a shopping basket and ordering system.

Attached is a screenshot of a site that has the colourfulness and playfulness that we are looking for. Please have a look.

The bike images attached are renderings from the CAD software, actual high res photos will be used when the site is developed.

The product logo is attached and MUST be used on the site. It must be BOLD and can be incorporated into the actual website design.

The site pages are:
Home
Gallery
Buy
Contact

Competitors:
www.brambleplay.example
www.quorvaride.example
I do not like either of their sites.

We only have one product at this time, so the site is to be focused on that product, not a whole catalog of products. It is really a single product with the ability to purchase.
Updates

Project Deadline Extended
Reason: I am extending this competition in order to give me more time to review each design and provide the feedback that the designers deserve.

Target Market(s)

Parents, children ages 1.5 - 5.

Industry/Entity Type

It Company

Colors
0555a3
eb1f27
9bcb3c
faed22
f78f20
f37022
e34197
a6459a
6b449b

Requirements
Must have
• Please use the logo attached, but feel free to use different colors.
Should not have
• Dull colors like black and grey

```html
<!DOCTYPE html>
<html lang="en">
<head>
<meta charset="utf-8">
<title>Zippa Loop Trike</title>
<link href="https://fonts.googleapis.com/css2?family=Source+Sans+3:wght@300;400;600;700&family=PT+Sans+Narrow:wght@700&display=swap" rel="stylesheet">
<style>
:root{
  --red:#e3312e;
  --red-dark:#cc2722;
  --page:#f6f6f6;
  --white:#ffffff;
  --ink:#333333;
  --body:#707070;
  --line:#e4e4e4;
  --btn-dark:#2c2c2c;
  --sky:#7cc7ea;
  --blue:#4f6fb3;
}
*{margin:0;padding:0;box-sizing:border-box}
html,body{width:1200px;height:1016px;overflow:hidden}
body{position:relative;background:var(--page);font-family:"Source Sans 3",Arial,sans-serif;color:var(--ink)}
.abs{position:absolute}
.topbar{left:0;top:0;width:1200px;height:50px;background:var(--white)}
.account-links{left:575px;top:20px;font-size:13px;color:#777;display:flex;gap:12px}
.search{left:723px;top:13px;width:248px;height:28px;border:1px solid #dcdcdc;border-radius:3px;background:var(--white);font-size:9px;color:#aaa;padding:8px 9px}
.search svg{position:absolute;right:8px;top:7px}
.login{left:992px;top:11px;width:78px;height:27px;background:linear-gradient(#7a7a7a,#5a5a5a);color:var(--white);font-weight:700;font-size:12px;text-align:center;line-height:27px}
.navband{left:0;top:50px;width:1200px;height:69px;background:var(--red)}
.nav-active{left:733px;top:50px;width:76px;height:69px;background:var(--red-dark)}
.nav-link{top:50px;height:69px;line-height:75px;color:var(--white);text-decoration:none;font-weight:600;font-size:19px;white-space:nowrap}
.brand{left:113px;top:26px;width:115px;height:115px;border-radius:50%;background:var(--white);border:4px solid var(--red);display:flex;align-items:center;justify-content:center;text-align:center;color:var(--red);font-weight:700;font-size:16px;line-height:1.1}
.slider{left:128px;top:159px;width:941px;height:365px;background:var(--white);border:1px solid var(--line)}
.kids-photo{left:160px;top:175px;width:389px;height:348px;background:radial-gradient(ellipse at 50% 45%,#f3c4a8 0%,#e7b89d 35%,#f8eef0 75%,#ffffff 100%)}
.video-title{left:589px;top:203px;font-weight:300;font-size:20px;color:#333;letter-spacing:-0.3px}
.video-frame{left:589px;top:234px;width:453px;height:255px;background:#ececec;border:1px solid #dcdcdc}
.video-still{left:597px;top:241px;width:437px;height:239px;background:linear-gradient(180deg,#5d7d3c 0%,#3a3fb8 45%,#2b2f96 70%,#6b8a4a 100%)}
.play{left:785px;top:349px;width:61px;height:37px;background:rgba(30,30,40,.75);border-radius:3px}
.controls{left:607px;top:446px;width:416px;height:28px;background:rgba(25,25,30,.7);border-radius:2px}
.arrow{top:284px;width:59px;height:84px;background:var(--red);display:flex;align-items:center;justify-content:center}
.welcome{left:129px;top:569px;font-weight:600;font-size:19px;letter-spacing:-0.2px}
.copy{left:129px;top:620px;width:620px;font-weight:300;font-size:14.4px;line-height:24px;color:var(--body);text-align:justify;letter-spacing:-0.15px}
.copy p+p{margin-top:6px}
.product{left:769px;top:562px;width:300px;height:296px;background:var(--red);color:var(--white)}
.product h2{position:absolute;left:14px;top:18px;font-size:19px;font-weight:600}
.product-frame{position:absolute;left:14px;top:63px;width:271px;height:161px;background:var(--white);padding:6px}
.product-photo{width:100%;height:100%;background:linear-gradient(180deg,#3f6d2c 0%,#8a9aa0 50%,#b8bcc0 75%,#5c7a3a 100%)}
.product-name{position:absolute;left:15px;top:235px;font-weight:700;font-size:14.5px}
.product-sub{position:absolute;left:16px;top:255px;font-weight:400;font-size:14.5px}
.buy-now{position:absolute;left:192px;top:238px;width:94px;height:33px;background:var(--btn-dark);border-radius:2px;font-family:"PT Sans Narrow",sans-serif;font-weight:700;font-size:15px;text-align:center;line-height:33px}
.footer{left:0;top:906px;width:1200px;height:110px;background:var(--red);color:var(--white)}
.footer-links{position:absolute;left:129px;top:21px;font-weight:600;font-size:15px;display:flex;gap:12px}
.copyright{position:absolute;left:129px;top:55px;font-weight:600;font-size:15px}
.social{position:absolute;top:37px;width:35px;height:35px;border-radius:50%}
</style>
</head>
<body>
<div class="abs topbar"></div>
<div class="abs account-links"><span>My Account</span><span>|</span><span>Cart (0)</span></div>
<div class="abs search">Type search
  <svg width="12" height="12" viewBox="0 0 12 12"><circle cx="5" cy="5" r="3.5" fill="none" stroke="#999" stroke-width="1.3"/><line x1="7.5" y1="7.5" x2="11" y2="11" stroke="#999" stroke-width="1.6"/></svg>
</div>
<div class="abs login">LOGIN</div>

<div class="abs navband"></div>
<div class="abs nav-active"></div>
<nav>
  <a class="abs nav-link" href="#" style="left:749px">Home</a>
  <a class="abs nav-link" href="#" style="left:837px">Gallery</a>
  <a class="abs nav-link" href="#" style="left:935px">Buy</a>
  <a class="abs nav-link" href="#" style="left:1005px">Contact</a>
</nav>
<div class="abs brand">Zippa<br>Loop<br>Trike</div>

<div class="abs arrow" style="left:69px"><svg width="20" height="32" viewBox="0 0 20 32"><polyline points="16,3 4,16 16,29" fill="none" stroke="#fff" stroke-width="5"/></svg></div>
<div class="abs arrow" style="left:1069px;width:53px"><svg width="20" height="32" viewBox="0 0 20 32"><polyline points="4,3 16,16 4,29" fill="none" stroke="#fff" stroke-width="5"/></svg></div>
<div class="abs slider"></div>
<div class="abs kids-photo" role="img" aria-label="Photo of four smiling children leaning together"></div>
<div class="abs video-title">Zippa Loop Trike&nbsp; Videos</div>
<div class="abs video-frame"></div>
<div class="abs video-still" role="img" aria-label="Video still of the blue ride-on trike on a park path"></div>
<div class="abs play"><svg width="61" height="37" viewBox="0 0 61 37"><polygon points="25,11 25,26 37,18.5" fill="#fff"/></svg></div>
<div class="abs controls">
  <svg width="416" height="28" viewBox="0 0 416 28">
    <rect x="8" y="10" width="305" height="8" fill="#222" stroke="#888"/>
    <rect x="9" y="11" width="240" height="6" fill="#6c6c6c"/>
    <rect x="9" y="11" width="86" height="6" fill="#1e9be0"/>
    <g fill="#1e9be0"><rect x="322" y="9" width="2" height="10"/><rect x="326" y="9" width="2" height="10"/><rect x="330" y="9" width="2" height="10"/><rect x="334" y="9" width="2" height="10"/><rect x="338" y="9" width="2" height="10"/><rect x="342" y="9" width="2" height="10"/><rect x="346" y="9" width="2" height="10"/></g>
    <text x="358" y="19" fill="#1e9be0" font-family="Source Sans 3,sans-serif" font-weight="700" font-style="italic" font-size="12">HD</text>
    <path d="M391 9l4 4M399 9l-4 4M391 19l4-4M399 19l-4-4" stroke="#ddd" stroke-width="2"/>
  </svg>
</div>

<h1 class="abs welcome">Welcome to Zippa Loop Trike</h1>
<div class="abs copy">
  <p>Lorem Ipsum is simply dummy text of the printing and typesetting industry. Lorem Ipsum has been the industry's standard dummy text ever since the 1500s, when an unknown printer took a galley of type and scrambled it to make a type specimen book. It has survived not only five centuries, but also the leap into electronic typesetting, remaining essentially unchanged. It was popularised in the 1960s with the release of Transfix sheets containing Lorem Ipsum passages, and more recently with desktop publishing software like Orvel PageForge including versions of Lorem Ipsum.</p>
  <p>Lorem Ipsum is simply dummy text of the printing and typesetting industry. Lorem Ipsum has been the industry's standard dummy text ever since the 1500s, when an unknown printer took a galley of type and scrambled it to make a type specimen book. It has survived not only five centuries, but also the leap into electronic typesetting, remaining essentially unchanged.</p>
</div>

<section class="abs product">
  <h2>Our Product</h2>
  <div class="product-frame"><div class="product-photo" role="img" aria-label="Rendering of the silver ride-on trike with red wheels in a park"></div></div>
  <div class="product-name">Zippa Loop Trike</div>
  <div class="product-sub">Lorem Ipsum is simply</div>
  <div class="buy-now">BUY NOW</div>
</section>

<footer class="abs footer">
  <div class="footer-links"><span>Home</span><span>|</span><span>Gallery</span><span>|</span><span>Buy</span><span>|</span><span>Contact</span></div>
  <div class="copyright">Copyright ©2013&nbsp; Company Name &nbsp;&nbsp;- All rights reserved</div>
  <div class="social" style="left:992px;background:var(--sky)" role="img" aria-label="Social link"></div>
  <div class="social" style="left:1034px;background:var(--blue)" role="img" aria-label="Social link"></div>
</footer>
</body>
</html>
```